Commercial Cleaning Company Needs A Flyer

We are a commercial cleaning company based in London.
We are currently trying to grow our client base and would like a fresh, professional flyer that differentiates us from the competition. We mainly specialises in commercial cleaning such as offices, educational facilities etc. I would like to see a flyer design that look professional, unique not cheap. I have attached a file that contains some company details but Im happy to explore other options if thay are relevant. Please also find company logo and colour chart, this should remain as is.

I have attached some pictures that contain diamond shaped windows. I feel that this can be used to represent and incorporate the logo. Please add to flyer where possible.

Please feel free to contact me for any further advice.
Thanks and good luck

Target Market(s)

commercial buildings and residential property owners

Industry/Entity Type

Cleaning Service

Contact Information for Business Card

Please refer to up loaded document for company details and logo colours.

Font styles to use
Sans Serif

Colors
33a6d7
33b8a4

Requirements
Must have
• Look Professional, not cheap, unique, stand out from others.

```html
<!DOCTYPE html>
<html lang="en">
<head>
<meta charset="utf-8">
<title>Clearpane Services – Flyer</title>
<link href="https://fonts.googleapis.com/css2?family=EB+Garamond:ital,wght@0,400;0,500;1,400&family=Montserrat:wght@400;600&display=swap" rel="stylesheet">
<style>
  :root{
    --blue:#33a6d7;
    --blue-deep:#1f8fc6;
    --teal:#33b8a4;
    --teal-deep:#2aa596;
    --ink:#1b1b1b;
    --white:#ffffff;
    --page:#e9e6e1;
  }
  *{box-sizing:border-box;margin:0;padding:0}
  html,body{width:1200px;height:1000px;overflow:hidden}
  body{background:var(--page);position:relative;font-family:"EB Garamond",Georgia,serif;color:var(--ink)}

  .flyer{position:absolute;left:229px;top:20px;width:741px;height:960px;background:var(--white);box-shadow:0 4px 18px rgba(0,0,0,.18);display:flex;overflow:hidden}
  .flyer-main{width:524px;height:100%;display:flex;flex-direction:column}
  .flyer-side{width:217px;height:100%;display:flex;flex-direction:column}

  /* header */
  .header{position:relative;height:430px;background:var(--white)}
  .city-illustration{position:absolute;left:0;right:0;top:80px;bottom:0;background:linear-gradient(180deg,#ffffff 0%,#e4e4e4 55%,#bdbdbd 100%)}
  .brand{position:absolute;left:24px;top:38px;display:flex;align-items:center;gap:10px;z-index:2}
  .brand-mark{width:26px;height:26px;border-radius:50%;background:var(--teal)}
  .brand-name{font-family:"EB Garamond",Georgia,serif;font-size:28px;font-weight:500;color:var(--teal);line-height:1}
  .slogan{position:absolute;left:26px;top:100px;z-index:2;font-size:19px;line-height:1.15}
  .slogan em{font-style:italic}

  /* about */
  .about{flex:1;background:var(--teal);color:var(--white);padding:12px 26px 0}
  .about h2{font-style:italic;font-weight:400;font-size:20px;margin-bottom:4px}
  .about p{font-size:10.2px;line-height:1.25;margin-bottom:12px}
  .guarantees{list-style:none;padding-left:44px;margin-top:-2px}
  .guarantees li{font-size:15px;line-height:1.27}
  .features{display:flex;justify-content:space-between;padding:30px 18px 0 54px}
  .feature{width:90px;text-align:center;font-family:"Montserrat",sans-serif;font-weight:600;font-size:10.5px;line-height:1.1}
  .feature-icon{width:56px;height:56px;border-radius:50%;background:var(--white);margin:0 auto 6px;display:flex;align-items:center;justify-content:center}
  .feature-icon svg{width:32px;height:32px}

  /* contact */
  .contact{height:77px;background:var(--white);padding:6px 24px 0}
  .contact-lead{font-size:11px;font-weight:500;margin-bottom:5px}
  .contact-row{display:flex;flex-wrap:wrap;gap:4px 18px;font-family:"Montserrat",sans-serif;font-size:12.5px}
  .contact-item{display:flex;align-items:center;gap:5px}
  .contact-item svg{width:12px;height:12px}

  /* side */
  .office-photo{height:365px;background:linear-gradient(160deg,#f3f5f7 0%,#cfd6dc 45%,#8e9aa4 80%,#5e6a73 100%)}
  .services{flex:1;background:linear-gradient(180deg,var(--blue-deep),var(--blue));color:var(--white);padding:20px 14px 0;font-family:"Montserrat",sans-serif}
  .services h3{font-size:13.5px;font-weight:600;margin-bottom:3px}
  .service-list{list-style:none;margin-bottom:22px}
  .service-list li{font-size:10.2px;line-height:1.27;padding-left:12px;position:relative}
  .service-list li::before{content:"\2665";position:absolute;left:0;top:0;font-size:9px}
  .social{display:flex;gap:8px;margin-top:14px}
  .social span{width:14px;height:14px;background:var(--white)}
</style>
</head>
<body>
<article class="flyer">
  <div class="flyer-main">
    <header class="header">
      <div class="city-illustration" role="img" aria-label="Line drawing of the London skyline with Tower Bridge, Big Ben and a curved glass tower"></div>
      <div class="brand">
        <span class="brand-mark"></span>
        <span class="brand-name">Clearpane Services</span>
      </div>
      <p class="slogan">Sparkling Service. Attention to Detail.<br><em>Human Support.</em></p>
    </header>

    <section class="about">
      <h2>About Us</h2>
      <p>Clearpane Services continual commitment and dedication to delivering a quality service has enabled us to build a solid foundation within the cleaning industry. Our principle and objectives are simple, provide our customers with an affordable quality service to suit their needs and always put our clients first.</p>
      <p>CPS rewards dependability, integrality and provide the training and development for all employees to achieve the best possible results. We believe that building relationships based on ethical conduct towards employees and clientele defines our unique working environments and is a vital key to our success.</p>
      <p>This is why at Clearpane Services stand behind our performance and guarantee your</p>
      <ul class="guarantees">
        <li>Quick response to costumers needs guaranteed</li>
        <li>Unequal attention to detail</li>
        <li>Affordable cleaning tailored to your needs</li>
        <li>Lengthy industry experience</li>
        <li>Insurance inclusive of workers compensation and liability</li>
        <li>Training provided to all staff and supervisors</li>
        <li>Your satisfaction is our priority</li>
      </ul>
      <div class="features">
        <div class="feature">
          <div class="feature-icon"><svg viewBox="0 0 32 32" fill="none" stroke="#33b8a4" stroke-width="2.2" stroke-linecap="round"><path d="M11 18a7 7 0 1 1 10 0c-1.5 1.5-2 2.5-2 4h-6c0-1.5-.5-2.5-2-4z"/><path d="M13 25h6M14 28h4M16 2v3M5 6l2 2M27 6l-2 2M2 15h3M27 15h3"/></svg></div>
          SPARKLING SERVICE
        </div>
        <div class="feature">
          <div class="feature-icon"><svg viewBox="0 0 32 32"><path d="M16 28 4 16a7 7 0 0 1 12-8 7 7 0 0 1 12 8z" fill="#33b8a4"/></svg></div>
          QUALITY CLEANERS
        </div>
        <div class="feature">
          <div class="feature-icon"><svg viewBox="0 0 32 32" fill="none" stroke="#33b8a4" stroke-width="2" stroke-linecap="round"><path d="M12 19a6 6 0 1 1 8 0c-1.2 1.2-1.6 2-1.6 3.4h-4.8c0-1.4-.4-2.2-1.6-3.4z"/><path d="M14 25h4M16 4v3M7 8l2 2M25 8l-2 2"/></svg></div>
          HUMAN SUPPORT
        </div>
        <div class="feature">
          <div class="feature-icon"><svg viewBox="0 0 32 32" fill="none" stroke="#33b8a4" stroke-width="2.2" stroke-linecap="round"><path d="M20 10v13a4 4 0 0 1-8 0V8a3 3 0 0 1 6 0v14a1 1 0 0 1-2 0V11"/></svg></div>
          COMPETITIVE PRICING
        </div>
      </div>
    </section>

    <footer class="contact">
      <p class="contact-lead">Would you like your office building assessed? We'll visit, give you a quote…. Contact Us at</p>
      <div class="contact-row">
        <span class="contact-item"><svg viewBox="0 0 12 12"><rect x="3" y="0.5" width="6" height="11" rx="1.2" fill="none" stroke="#33a6d7" stroke-width="1.2"/></svg>07700 900412</span>
        <span class="contact-item"><svg viewBox="0 0 12 12"><circle cx="6" cy="6" r="5.3" fill="none" stroke="#33a6d7" stroke-width="1.1"/><path d="M4 3.5l1 1.5-.6.8a4 4 0 0 0 1.8 1.8l.8-.6 1.5 1-.6 1.2C5.6 9 3 6.4 3 4.1z" fill="#33a6d7"/></svg>020 7946 0318</span>
        <span class="contact-item"><svg viewBox="0 0 12 12" fill="none" stroke="#33a6d7" stroke-width="1"><circle cx="6" cy="6" r="5"/><ellipse cx="6" cy="6" rx="2.2" ry="5"/><path d="M1 6h10"/></svg>clearpaneservices.co.uk</span>
        <span class="contact-item"><svg viewBox="0 0 12 12" fill="none" stroke="#33a6d7" stroke-width="1.1"><rect x="0.8" y="2.5" width="10.4" height="7"/><path d="M1 3l5 3.8L11 3"/></svg>hello@clearpaneservices.co.uk</span>
      </div>
    </footer>
  </div>

  <aside class="flyer-side">
    <div class="office-photo" role="img" aria-label="Photograph of a bright modern office interior with curved diamond-grid glass windows"></div>
    <div class="services">
      <h3>Commercial Cleaning</h3>
      <ul class="service-list">
        <li>Offices</li><li>Education Facilities</li><li>Medical Facilities</li><li>Restaurants</li><li>Showroom</li>
      </ul>
      <h3>Services</h3>
      <ul class="service-list">
        <li>General Cleaning Requirements</li><li>Consumables supply and replacement</li><li>Washroom services</li><li>Building maintenance</li><li>Window cleaning</li><li>Carpet care</li><li>Floor maintenance</li><li>Scrubbing machinery</li><li>PAT Testing</li><li>Waste removal</li><li>Recycling Programs</li>
      </ul>
      <h3>Residential Cleaning</h3>
      <ul class="service-list">
        <li>House Cleaning</li><li>Apartment Cleaning</li><li>Move In/Out Cleaning</li><li>After Event Cleaning</li><li>Spring Cleaning</li><li>Post Building Works</li><li>Deep Clean</li>
      </ul>
      <h3>Green Cleaning Available</h3>
      <ul class="service-list">
        <li>No harmful chemicals</li><li>Safe for children and pets</li><li>Eco-friendly</li><li>No artificial fragrances</li>
      </ul>
      <div class="social"><span></span><span></span><span></span><span></span></div>
    </div>
  </aside>
</article>
</body>
</html>
```